Business Card for Web Design consulting firm

Business card designs for Web Design consulting firm

Target Market(s)

English speaking adults ages 30 - 60. Predominantly professional services eg. Doctor, Dentist

Industry/Entity Type

Consulting

Requirements
Must have
• Double sided card

```html
<!DOCTYPE html>
<html lang="en">
<head>
<meta charset="utf-8">
<title>Corvane – Business Card</title>
<link rel="stylesheet" href="https://fonts.googleapis.com/css2?family=Open+Sans:wght@400;600;700&display=swap">
<style>
  :root {
    --charcoal: #3f4447;
    --orange: #f7881c;
    --ink: #3a3d3f;
    --page: #ffffff;
  }
  * { box-sizing: border-box; margin: 0; padding: 0; }
  html, body {
    width: 1200px;
    height: 1046px;
    overflow: hidden;
    background: var(--page);
    font-family: "Open Sans", Arial, sans-serif;
  }
  .canvas { position: relative; width: 1200px; height: 1046px; }

  .card {
    position: absolute;
    overflow: hidden;
    background: var(--orange);
  }

  /* Front side */
  .card-front { left: 120px; top: 145px; width: 605px; height: 325px; }
  .card-front .diagonal { position: absolute; inset: 0; width: 100%; height: 100%; }
  .card-front .brand {
    position: absolute;
    left: 178px;
    top: 170px;
    display: flex;
    align-items: center;
    gap: 16px;
  }
  .brand-square { width: 26px; height: 26px; background: var(--charcoal); }
  .brand-name {
    color: var(--charcoal);
    font-weight: 600;
    font-size: 44px;
    letter-spacing: 6px;
    line-height: 1;
  }

  /* Back side */
  .card-back { left: 455px; top: 570px; width: 600px; height: 343px; }
  .card-back .top-band {
    position: absolute; left: 0; top: 0; width: 100%; height: 75px;
    background: var(--charcoal);
  }
  .card-back .brand {
    position: absolute; left: 42px; top: 96px;
    display: flex; align-items: center; gap: 10px;
  }
  .card-back .brand-square { width: 18px; height: 18px; }
  .card-back .brand-name { font-size: 30px; letter-spacing: 4px; }

  .holder-name {
    position: absolute; right: 48px; top: 30px;
    color: var(--orange); font-weight: 700; font-size: 32px; line-height: 1;
  }
  .holder-title {
    position: absolute; right: 48px; top: 84px;
    color: var(--ink); font-size: 19px; line-height: 1;
  }

  .address, .contact {
    position: absolute; top: 166px;
    color: var(--ink); font-size: 19px; line-height: 28px;
    list-style: none;
  }
  .address { left: 40px; }
  .contact { right: 48px; text-align: right; }

  .web {
    position: absolute; left: 0; right: 0; top: 302px;
    text-align: center; color: var(--ink); font-size: 19px;
  }
</style>
</head>
<body>
<main class="canvas">

  <section class="card card-front" aria-label="Card front">
    <svg class="diagonal" viewBox="0 0 605 325" preserveAspectRatio="none" aria-hidden="true">
      <polygon points="0,0 555,0 0,267" fill="var(--charcoal)"/>
    </svg>
    <div class="brand">
      <span class="brand-square"></span>
      <span class="brand-name">CORVANE</span>
    </div>
  </section>

  <section class="card card-back" aria-label="Card back">
    <div class="top-band"></div>
    <div class="brand">
      <span class="brand-square"></span>
      <span class="brand-name">CORVANE</span>
    </div>
    <h1 class="holder-name">Daniel Reyes</h1>
    <p class="holder-title">Job title</p>
    <ul class="address">
      <li>Address 1</li>
      <li>Address 2</li>
      <li>Address 3</li>
    </ul>
    <ul class="contact">
      <li>E-mail</li>
      <li>Phone</li>
      <li>Cell</li>
      <li>Fax</li>
    </ul>
    <p class="web">Web Address</p>
  </section>

</main>
</body>
</html>
```